Uprising SaaS company needs an attractive business card design

We're an uprising SaaS company who's attempting to attack the rigid car (insurance) claims management market in Europe.
We want to our mighty base order management system, listen to our clients to connect the smart ideas to build something even mightier.
We primarily focus on helping our customers manage their customers' claims/orders and get them resolved as smoothly as possible.
We'd like the business card design to express technical innovation and the fact that we connect smart ideas, as our company slogan indicates.
Contact Information for Business Card
Name, position, website, email, mobile, business address
Font styles to use
Colors
Designer to choose colors to be used in the design.
Look and feel
Each slider illustrates characteristics of the customer's brand and the style your logo design should communicate.

```html
<!DOCTYPE html>
<html lang="en">
<head>
<meta charset="UTF-8">
<title>Synvora Business Card</title>
<link href="https://fonts.googleapis.com/css2?family=Open+Sans:wght@300;400;600&display=swap" rel="stylesheet">
<style>
  :root {
    --page: #ffffff;
    --card: #0b0830;
    --pattern: #3a3d6e;
    --white: #ffffff;
    --muted: #c9cbd8;
    --icon: #8fb6c4;
    --divider: #3c3f66;
    --brand: #6fc1d4;
  }
  * { margin: 0; padding: 0; box-sizing: border-box; }
  html, body {
    width: 1200px; height: 1200px; overflow: hidden;
    background: var(--page);
    font-family: "Open Sans", Arial, sans-serif;
  }
  .canvas { position: relative; width: 1200px; height: 1200px; }
  .card {
    position: absolute; left: 206px; width: 788px; height: 448px;
    background: var(--card); overflow: hidden;
    box-shadow: 0 6px 18px rgba(0,0,0,0.28);
  }
  .card--front { top: 110px; }
  .card--back { top: 642px; }

  .pattern { position: absolute; }
  .card--front .pattern {
    right: 0; top: 0; width: 440px; height: 300px;
    background: radial-gradient(ellipse at 100% 0%, rgba(90,95,150,0.45) 0%, rgba(60,64,110,0.18) 45%, rgba(11,8,48,0) 75%);
  }
  .card--back .pattern {
    left: 0; bottom: 0; width: 788px; height: 448px;
    background: linear-gradient(to top, rgba(70,74,125,0.35) 0%, rgba(50,54,100,0.12) 40%, rgba(11,8,48,0) 70%);
  }

  .identity { position: absolute; left: 86px; top: 74px; }
  .identity__name {
    color: var(--white); font-weight: 600; font-size: 38px; line-height: 1;
    letter-spacing: 0.5px;
  }
  .identity__company {
    margin-top: 14px; color: var(--muted); font-weight: 400; font-size: 20px;
    letter-spacing: 12px; line-height: 1;
  }

  .contacts { position: absolute; left: 0; top: 290px; width: 788px; height: 120px; }
  .contact {
    position: absolute; top: 0; width: 164px; height: 120px;
    text-align: center;
  }
  .contact svg { display: block; margin: 20px auto 0; width: 30px; height: 30px; }
  .contact__text {
    margin-top: 22px; color: var(--muted); font-size: 14px; line-height: 1;
  }
  .contact--phone { left: 66px; }
  .contact--mail { left: 230px; }
  .contact--web { left: 394px; }
  .contact--address { left: 556px; }
  .divider {
    position: absolute; top: 0; width: 2px; height: 116px; background: var(--divider);
  }
  .divider--1 { left: 230px; }
  .divider--2 { left: 394px; }
  .divider--3 { left: 558px; }

  .brandmark {
    position: absolute; left: 0; top: 180px; width: 788px; text-align: center;
    color: var(--brand); font-weight: 300; font-size: 84px; line-height: 1;
    letter-spacing: 1px;
  }
</style>
</head>
<body>
<div class="canvas">
  <section class="card card--front">
    <div class="pattern" role="img" aria-label="Faint triangle pattern fading from the top right corner"></div>
    <div class="identity">
      <div class="identity__name">YOUR NAME</div>
      <div class="identity__company">SYNVORA</div>
    </div>
    <div class="contacts">
      <div class="divider divider--1"></div>
      <div class="divider divider--2"></div>
      <div class="divider divider--3"></div>
      <div class="contact contact--phone">
        <svg viewBox="0 0 24 24" aria-hidden="true"><path fill="var(--icon)" d="M6.6 10.8a15.1 15.1 0 0 0 6.6 6.6l2.2-2.2c.3-.3.7-.4 1-.2 1.1.4 2.3.6 3.6.6.6 0 1 .4 1 1V20c0 .6-.4 1-1 1A17 17 0 0 1 3 4c0-.6.4-1 1-1h3.5c.6 0 1 .4 1 1 0 1.3.2 2.5.6 3.6.1.3 0 .7-.2 1z"/></svg>
        <div class="contact__text">+0123 4567 8900</div>
      </div>
      <div class="contact contact--mail">
        <svg viewBox="0 0 24 24" aria-hidden="true"><rect x="3" y="5.5" width="18" height="13" rx="1.5" fill="none" stroke="var(--icon)" stroke-width="2"/><path d="M3.5 6.5l8.5 6.5 8.5-6.5" fill="none" stroke="var(--icon)" stroke-width="2"/></svg>
        <div class="contact__text">Mail@synvora.com</div>
      </div>
      <div class="contact contact--web">
        <svg viewBox="0 0 24 24" aria-hidden="true" fill="none" stroke="var(--icon)" stroke-width="1.6"><circle cx="12" cy="12" r="9"/><ellipse cx="12" cy="12" rx="4" ry="9"/><path d="M3 12h18M4.5 7.5h15M4.5 16.5h15"/></svg>
        <div class="contact__text">www.website.com</div>
      </div>
      <div class="contact contact--address">
        <svg viewBox="0 0 24 24" aria-hidden="true"><path fill="var(--icon)" d="M12 2a7 7 0 0 0-7 7c0 5.2 7 13 7 13s7-7.8 7-13a7 7 0 0 0-7-7zm0 9.5A2.5 2.5 0 1 1 12 6.5a2.5 2.5 0 0 1 0 5z"/></svg>
        <div class="contact__text">Company Address</div>
      </div>
    </div>
  </section>

  <section class="card card--back">
    <div class="pattern" role="img" aria-label="Faint triangle pattern rising from the bottom edge"></div>
    <div class="brandmark">synvora</div>
  </section>
</div>
</body>
</html>
```